Plum & Us Business Card Design

Plum & Us is a company that makes treats and real food for people with food allergies, illnesses and those that like to eat clean. We like to take good old fashioned favorites and create a clean, healthy version of it without losing any of the addictive ‘yumminess’ of it.All of our products are made with Organic ingredients and we aim to be as sustainable as possible therefore I would like this to be reflected in our business cards. I like the thought of using chia seeds in the business card maybe so that people could grow their own.

Industry/Entity Type

Health And Wellness

Contact Information for Business Card

Plum & Uswww.plumandus.com.aumarnie@plumandus.com.auP: 0431 596 218 Facebook and Instagram logos

Requirements
Must have
• Logo - does not have to be the exact logo as long as it is close and fits in with the other information I have asked for (sustainable & Organic, recycled etc.)
• See the photo with the treats for a picture of the logo

```html
<!DOCTYPE html>
<html lang="en">
<head>
<meta charset="utf-8">
<title>Plum &amp; Us Business Card</title>
<link href="https://fonts.googleapis.com/css2?family=Open+Sans:wght@400;700&display=swap" rel="stylesheet">
<style>
  :root {
    --paper-light: #dccaa8;
    --paper-mid: #cfb994;
    --paper-dark: #bda37c;
    --leaf-green: #248a3a;
    --leaf-green-deep: #1c7a32;
    --brand-navy: #2b2a6b;
    --title-green: #173d17;
    --ink: #141414;
  }
  html, body {
    margin: 0;
    padding: 0;
    overflow: hidden;
    background: #ffffff;
  }
  .card {
    position: relative;
    width: 1200px;
    height: 740px;
    overflow: hidden;
    font-family: "Open Sans", Arial, sans-serif;
  }
  .card__paper {
    position: absolute;
    inset: 0;
    background: radial-gradient(ellipse at 40% 40%, var(--paper-light) 0%, var(--paper-mid) 60%, var(--paper-dark) 100%);
  }
  .card__leaf-art {
    position: absolute;
    left: 368px;
    top: 78px;
    width: 752px;
    height: 662px;
    border-top-left-radius: 100% 100%;
    background: linear-gradient(160deg, var(--leaf-green) 0%, var(--leaf-green-deep) 100%);
  }
  .brand-name {
    position: absolute;
    left: 70px;
    top: 96px;
    margin: 0;
    font-size: 104px;
    font-weight: 400;
    line-height: 1;
    color: var(--brand-navy);
  }
  .contact {
    position: absolute;
    right: 145px;
    top: 274px;
    text-align: right;
    color: var(--ink);
  }
  .contact__title {
    margin: 0 0 8px;
    font-size: 41px;
    font-weight: 700;
    line-height: 1.2;
    color: var(--title-green);
  }
  .contact__line {
    margin: 0;
    font-size: 30px;
    font-weight: 400;
    line-height: 42px;
  }
  .social {
    display: flex;
    justify-content: flex-end;
    gap: 46px;
    margin-top: 16px;
    margin-right: 10px;
  }
  .social__circle {
    width: 52px;
    height: 52px;
    border-radius: 50%;
    background: var(--ink);
  }
  .social__square {
    width: 46px;
    height: 46px;
    margin-top: 3px;
    border-radius: 8px;
    background: var(--ink);
  }
</style>
</head>
<body>
  <main class="card">
    <div class="card__paper" role="img" aria-label="Recycled parchment paper texture"></div>
    <div class="card__leaf-art" role="img" aria-label="Two large overlapping green leaves with dark outlines"></div>

    <h1 class="brand-name">Plum &amp; Us</h1>

    <section class="contact">
      <p class="contact__title">PLUM &amp; US</p>
      <p class="contact__line">P : 0431 596 218</p>
      <p class="contact__line">www.plumandus.com.au</p>
      <p class="contact__line">marnie@plumandus.com.au</p>
      <div class="social">
        <span class="social__circle" role="img" aria-label="Social profile"></span>
        <span class="social__square" role="img" aria-label="Social profile"></span>
      </div>
    </section>
  </main>
</body>
</html>
```